PELDRAX Business Cards

We require a business card for our company that provides IT consulting services. We already have a logo that needs to be used on the card. We want a clean professional looking design that incorporates our colours. Our main focus is providing managed services to business, which involves us looking after all of their IT requirements including managing servers/networks, projects, and procurement.

Industry/Entity Type

Information Technology

Requirements
Must have
• our logo, contact information, name, title, phone numbers

```html
<!DOCTYPE html>
<html lang="en">
<head>
<meta charset="utf-8">
<title>PELDRAX Business Cards</title>
<link rel="stylesheet" href="https://fonts.googleapis.com/css2?family=Roboto:wght@400;500;700&display=swap">
<style>
  :root {
    --backdrop: #2a2a2a;
    --paper: #f4f4f4;
    --brand-blue: #1f97d4;
    --brand-blue-light: #3aa6dc;
    --ink: #222222;
    --white: #ffffff;
  }
  * { margin: 0; padding: 0; box-sizing: border-box; }
  html, body {
    width: 1200px;
    height: 1200px;
    overflow: hidden;
    background: var(--backdrop);
    font-family: "Roboto", Arial, sans-serif;
  }
  .canvas { position: relative; width: 1200px; height: 1200px; }

  .card {
    position: absolute;
    top: 186px;
    width: 454px;
    height: 792px;
    border-radius: 17px;
    overflow: hidden;
  }
  .card-front { left: 122px; background: var(--paper); }
  .card-back { left: 612px; background: var(--brand-blue); }

  /* front */
  .brand-lockup {
    position: absolute;
    top: 60px;
    left: 0;
    right: 0;
    display: flex;
    align-items: center;
    justify-content: center;
    gap: 14px;
  }
  .brand-dot {
    width: 52px; height: 52px;
    border-radius: 50%;
    background: var(--brand-blue);
  }
  .brand-name {
    font-weight: 700;
    font-size: 54px;
    letter-spacing: 3px;
    color: var(--brand-blue);
    line-height: 1;
  }
  .person {
    position: absolute;
    top: 258px;
    left: 0; right: 0;
    text-align: center;
  }
  .person-name {
    font-weight: 700;
    font-size: 34px;
    color: var(--brand-blue);
    letter-spacing: 0.5px;
    line-height: 1;
  }
  .person-title {
    margin-top: 8px;
    font-size: 17px;
    color: var(--ink);
    letter-spacing: 0.5px;
  }
  .contact-list {
    position: absolute;
    top: 398px;
    left: 0; right: 0;
    list-style: none;
    text-align: center;
  }
  .contact-item { height: 86px; }
  .contact-icon {
    display: block;
    margin: 0 auto 6px;
    width: 38px; height: 38px;
  }
  .contact-text {
    font-size: 19px;
    color: var(--ink);
    letter-spacing: 0.6px;
  }
  .address-band {
    position: absolute;
    left: 0; right: 0; bottom: 0;
    height: 96px;
    background: linear-gradient(180deg, var(--brand-blue-light), var(--brand-blue));
    color: var(--white);
    text-align: center;
    font-size: 19px;
    letter-spacing: 0.6px;
    line-height: 23px;
    padding-top: 24px;
  }

  /* back */
  .back-mark {
    position: absolute;
    top: 210px;
    left: 0; right: 0;
    display: flex;
    flex-direction: column;
    align-items: center;
    gap: 34px;
  }
  .back-dot {
    width: 110px; height: 110px;
    border-radius: 50%;
    background: var(--white);
  }
  .back-name {
    font-weight: 700;
    font-size: 84px;
    letter-spacing: 4px;
    color: var(--white);
    line-height: 1;
  }
  .back-web {
    position: absolute;
    left: 218px;
    top: 698px;
    transform-origin: 0 0;
    transform: rotate(-90deg);
    font-size: 18px;
    line-height: 20px;
    letter-spacing: 2px;
    color: var(--white);
    white-space: nowrap;
  }
  .back-rule {
    position: absolute;
    left: 228px;
    top: 712px;
    width: 2px;
    height: 80px;
    background: var(--white);
  }
</style>
</head>
<body>
<main class="canvas">
  <section class="card card-front" aria-label="Card front">
    <div class="brand-lockup">
      <span class="brand-dot"></span>
      <span class="brand-name">PELDRAX</span>
    </div>

    <div class="person">
      <p class="person-name">DANIEL HART</p>
      <p class="person-title">CLU, ChFc, RFC</p>
    </div>

    <ul class="contact-list">
      <li class="contact-item">
        <svg class="contact-icon" viewBox="0 0 38 38" aria-hidden="true">
          <circle cx="19" cy="19" r="17" fill="none" stroke="#1f97d4" stroke-width="2.4"/>
          <path d="M14 11.5c1-.6 2 .2 2.6 1.3l1 1.9c.4.9 0 1.6-.7 2.1l-.8.6c.7 1.8 2.2 3.5 4 4.3l.6-.8c.5-.7 1.3-1 2.1-.6l1.9 1c1.1.6 1.8 1.6 1.2 2.6-.9 1.6-2.7 2.3-4.4 1.6-4.3-1.7-7.6-5-9.2-9.3-.6-1.7.1-3.6 1.7-4.7z" fill="#1f97d4"/>
        </svg>
        <span class="contact-text">(414) 555-0187</span>
      </li>
      <li class="contact-item">
        <svg class="contact-icon" viewBox="0 0 38 38" aria-hidden="true">
          <circle cx="19" cy="19" r="17" fill="none" stroke="#1f97d4" stroke-width="2.4"/>
          <rect x="10.5" y="13" width="17" height="12" rx="1" fill="#1f97d4"/>
          <path d="M11 13.8l8 6.2 8-6.2" fill="none" stroke="#f4f4f4" stroke-width="1.4"/>
        </svg>
        <span class="contact-text">dan@peldrax-it.com</span>
      </li>
      <li class="contact-item">
        <svg class="contact-icon" viewBox="0 0 38 38" aria-hidden="true">
          <circle cx="19" cy="19" r="17" fill="none" stroke="#1f97d4" stroke-width="2.4"/>
          <g fill="none" stroke="#1f97d4" stroke-width="1.4">
            <circle cx="19" cy="19" r="8.5"/>
            <ellipse cx="19" cy="19" rx="3.8" ry="8.5"/>
            <line x1="10.5" y1="19" x2="27.5" y2="19"/>
            <line x1="12" y1="14.5" x2="26" y2="14.5"/>
            <line x1="12" y1="23.5" x2="26" y2="23.5"/>
          </g>
        </svg>
        <span class="contact-text">www.peldrax-it.com</span>
      </li>
    </ul>

    <div class="address-band">
      <p>1875 Harbor Lane</p>
      <p>Lakeview, WI 53190</p>
    </div>
  </section>

  <section class="card card-back" aria-label="Card back">
    <div class="back-mark">
      <span class="back-dot"></span>
      <span class="back-name">PELDRAX</span>
    </div>
    <p class="back-web">www.peldrax.com</p>
    <span class="back-rule"></span>
  </section>
</main>
</body>
</html>
```